Website Design Brief for KBR LEGAL PTY LTD

Company Name: KBR LEGAL PTY LTD

Industry: Legal Services

Target Audience:

Corporate clients
Business owners
Individuals seeking legal advice in Commercial Law, Mergers and Acquisitions, Will Law, Property Law, and Conveyancing
Objective:

To create a professional, user-friendly website that establishes trust and authority in the legal field.
Provide easy access to information about the firm’s services, team, and areas of expertise.
Include client testimonials, contact information, and a blog or resource section for legal insights.
Key Features and Pages:

Homepage:

Clean, modern design with a professional feel.
Introduction to KBR LEGAL with a brief overview of services.
High-quality images or illustrations related to law and professionalism.
Prominent call-to-action (CTA) like "Get in Touch" or "Book a Consultation."
About Us:

Information about the firm's mission, values, and team.
Highlight the expertise and experience of key members.
Include a brief company history, if relevant.
Services:

Detailed descriptions of services, categorized by legal areas (e.g., Commercial Law, Mergers & Acquisitions, Property Law, etc.).
Call-to-action buttons to encourage potential clients to reach out for consultations.
Team:

Profiles of key team members, including their qualifications, expertise, and professional photos.
Include links to their professional networks (LinkedIn).
Testimonials:

Section showcasing positive client testimonials or case studies.
This can help build trust and credibility with potential clients.
Blog or Resources:

A blog or resources section providing legal tips, industry news, and insights.
Content should demonstrate the firm’s knowledge and thought leadership.
Contact Us:

Easy-to-use contact form.
Include phone number, email, physical office address, and possibly a map.
Option for booking consultations or initial meetings directly online.
Client Portal (optional):

Secure login for clients to access their case information, documents, and updates (this could be an advanced feature to consider after launch).
Design Aesthetic:

Clean, modern, and professional.
Elegant use of fonts and a color palette that reflects trust, authority, and sophistication (dark blues, whites, grays).
User-friendly navigation to ensure clients can easily find the information they need.
Technical Considerations:

The website should be mobile-responsive and look great on all devices (desktop, tablet, mobile).
Ensure fast load times and optimized images.
Implement SEO best practices to improve search engine rankings.
Easy-to-update CMS (WordPress or similar) to allow easy future updates.
Competitor/Inspirational Websites:

[Provide examples of legal firms' websites you like, or any designs that reflect the feel you want for your firm.]
Additional Information:

Please ensure all content is aligned with the firm's professional tone and approach.
The website should be designed to be scalable for future growth (adding more services, resources, etc.).

Target Market(s)

Business owners Individuals seeking legal advice in Commercial Law, Mergers and Acquisitions, Will Law, Property Law, and Conveyancing

Industry/Entity Type

Legal

Number of Pages Required

3 page

Requirements
Must have
• Home Page, About Us, Contact Us, Services

```html
<!DOCTYPE html>
<html lang="en">
<head>
<meta charset="utf-8">
<title>KBR LEGAL</title>
<link href="https://fonts.googleapis.com/css2?family=Roboto:wght@500;700;900&family=Lato:wght@400;700&display=swap" rel="stylesheet">
<style>
:root{
  --green:#2e8b2e;
  --green-dark:#226f22;
  --ink:#1e1e20;
  --dark:#231f20;
  --text:#777;
  --light-green:#eef5ea;
  --white:#fff;
  --footer:#1d1f22;
}
*{margin:0;padding:0;box-sizing:border-box}
html,body{width:1200px;height:3999px;overflow:hidden}
body{position:relative;font-family:'Lato',sans-serif;color:var(--ink);background:var(--white)}
.abs{position:absolute}
h2.section-title{position:absolute;left:0;width:1200px;text-align:center;font-family:'Roboto',sans-serif;font-weight:700;font-size:37px;letter-spacing:.3px;color:var(--ink)}
h2 .accent{color:var(--green)}
.title-rule{position:absolute;height:2px;background:var(--green)}
.lead{position:absolute;left:0;width:1200px;text-align:center;font-size:15.5px;line-height:29px;color:var(--text)}
.btn{position:absolute;background:var(--dark);color:#fff;font-weight:700;font-size:15px;display:flex;align-items:center;justify-content:center;clip-path:polygon(0 0,88% 0,100% 100%,0 100%)}

/* header */
.topbar{top:0;left:0;width:1200px;height:95px}
.contact-chip{position:absolute;top:24px;display:flex;gap:22px;align-items:center}
.chip-icon{width:45px;height:45px;background:var(--dark);display:flex;align-items:center;justify-content:center}
.chip-label{font-size:12px;font-weight:700}
.chip-value{font-size:19px;font-weight:700;margin-top:4px}
.brand{position:absolute;top:20px;left:486px;font-family:'Roboto',sans-serif;font-weight:500;font-size:44px;letter-spacing:1px;color:var(--dark)}
.nav{top:95px;left:0;width:1200px;height:51px;background:var(--green);display:flex;align-items:center;padding-left:110px;gap:0}
.nav a{color:#fff;text-decoration:none;font-size:15px;margin-right:66px}

/* hero */
.hero{top:146px;left:0;width:1200px;height:495px;background:linear-gradient(100deg,#c9d3dc 0%,#9fb2c4 45%,#5d7896 70%,#b5c3cf 100%)}
.hero-kicker{top:282px;left:110px;color:#fff;font-family:'Roboto',sans-serif;font-weight:700;font-size:23px}
.hero-title{top:312px;left:107px;color:#fff;font-family:'Roboto',sans-serif;font-weight:700;font-size:66px}
.hero-sub{top:388px;left:110px;color:#fff;font-weight:700;font-size:15.5px;line-height:31px}

/* trust cards */
.trust-card{position:absolute;top:905px;width:249px;height:278px;background:#fff;box-shadow:0 4px 22px rgba(0,0,0,.08);text-align:center;padding-top:32px}
.trust-card.active{border-bottom:3px solid var(--green)}
.trust-card h3{font-size:15px;font-weight:700;margin-top:16px}
.trust-card p{font-size:13px;line-height:24px;color:var(--text);margin:10px 18px 0}
.trust-card a{display:inline-block;margin-top:6px;font-size:13px;font-weight:700;color:var(--green)}

/* about */
.about-copy{left:689px;width:405px;font-size:15px;line-height:29px;color:var(--text)}
.about-title{left:689px;top:1320px;font-family:'Roboto',sans-serif;font-weight:700;font-size:37px}

/* services */
.services{top:1816px;left:0;width:1200px;height:664px;background:var(--light-green)}
.service-card{position:absolute;top:2039px;height:315px;background:#fff;text-align:center;padding:3px}
.service-card.active{border:2px solid var(--green)}
.service-media{height:183px}
.service-card h3{font-family:'Roboto',sans-serif;font-size:15px;font-weight:700;margin-top:23px}
.service-card.active h3{color:var(--green)}
.service-card p{font-size:13px;line-height:24px;color:var(--text);margin:6px 18px 0}
.round-arrow{position:absolute;width:42px;height:42px;border-radius:50%;display:flex;align-items:center;justify-content:center}

/* testimonials */
.reviews{top:2480px;left:0;width:1200px;height:464px}
.review-card{position:absolute;top:2645px;width:465px;height:240px;background:#fff}
.review-avatar{position:absolute;left:30px;top:32px;width:118px;height:118px;border-radius:50%}
.quote-badge{position:absolute;left:74px;top:136px;width:30px;height:30px;border-radius:50%;background:var(--green);color:#fff;display:flex;align-items:center;justify-content:center;font-weight:900;font-family:'Roboto',sans-serif;font-size:18px}
.review-text{position:absolute;left:171px;top:32px;width:262px;font-size:12.5px;line-height:25px;color:var(--text);text-align:justify}
.review-name{position:absolute;left:171px;top:172px;font-size:14px;font-weight:700}
.review-time{position:absolute;left:171px;top:196px;font-size:12px;color:var(--text)}
.stars{color:#f0a400;font-size:11px;margin-left:18px;letter-spacing:1px}

/* experts */
.expert-card{position:absolute;top:3189px;width:228px;height:306px;background:#fff;box-shadow:0 4px 22px rgba(0,0,0,.08);text-align:center;padding-top:36px}
.expert-card.active{border:2px solid var(--green);box-shadow:none}
.expert-photo{width:96px;height:96px;border-radius:50%;margin:0 auto}
.expert-card h3{font-family:'Roboto',sans-serif;font-weight:700;font-size:17px;margin-top:18px}
.expert-role{font-size:13px;color:var(--text);margin-top:4px}
.expert-card p{font-size:12.5px;line-height:22px;color:var(--text);margin:12px 20px 0}

/* footer */
.footer{top:3655px;left:0;width:1200px;height:300px;background:var(--footer);color:#fff}
.footer h4{position:absolute;top:58px;font-family:'Roboto',sans-serif;font-weight:700;font-size:18px}
.footer ul{position:absolute;list-style:none;font-size:15px}
.footer li{height:32.5px;display:flex;align-items:center;gap:16px}
.social{position:absolute;top:155px;width:34px;height:34px;background:var(--green)}
.copyright{top:3955px;left:0;width:1200px;height:44px;background:var(--green);color:#fff;font-size:13px;display:flex;align-items:center;justify-content:center}
</style>
</head>
<body>

<!-- header -->
<header class="abs topbar">
  <div class="contact-chip" style="left:110px">
    <div class="chip-icon"><svg width="16" height="16" viewBox="0 0 24 24"><path fill="#fff" d="M6.6 10.8a15 15 0 006.6 6.6l2.2-2.2c.3-.3.7-.4 1-.2 1.1.4 2.3.6 3.6.6.6 0 1 .4 1 1V20c0 .6-.4 1-1 1A17 17 0 013 4c0-.6.4-1 1-1h3.5c.6 0 1 .4 1 1 0 1.3.2 2.5.6 3.6.1.3 0 .7-.2 1z"/></svg></div>
    <div><div class="chip-label">Call Us:</div><div class="chip-value">+1 555 014 (2390)</div></div>
  </div>
  <div class="brand">KBR LEGAL</div>
  <div class="contact-chip" style="left:856px">
    <div class="chip-icon"><svg width="16" height="14" viewBox="0 0 24 20"><path fill="#fff" d="M2 2h20v16H2z"/><path fill="none" stroke="#231f20" stroke-width="2" d="M2 3l10 8 10-8"/></svg></div>
    <div><div class="chip-label">Email Us:</div><div class="chip-value">info@kbrlegal-demo.com</div></div>
  </div>
</header>
<nav class="abs nav">
  <a>Home</a><a>About KBR Legal</a><a>What We Provide</a><a>Why Choose Us?</a><a>Testimonials</a><a>Blogs</a><a style="margin-right:0">Contact Us</a>
</nav>

<!-- hero -->
<section class="abs hero" role="img" aria-label="Photograph of a modern glass office building against a cloudy sky"></section>
<svg class="abs" style="top:146px;left:0" width="1200" height="495">
  <defs><linearGradient id="heroGreen" x1="0" y1="0" x2="0" y2="1"><stop offset="0" stop-color="#2e8b2e" stop-opacity=".95"/><stop offset="1" stop-color="#2e8b2e" stop-opacity=".55"/></linearGradient></defs>
  <polygon points="0,88 473,88 559,405 0,405" fill="url(#heroGreen)"/>
</svg>
<div class="abs hero-kicker">WELCOME TO</div>
<h1 class="abs hero-title">KBR LEGAL</h1>
<p class="abs hero-sub">Specializing in Commercial Law, Mergers &amp; Acquisitions,<br>Will Law, Property Law, and Conveyancing</p>
<div class="btn" style="top:462px;left:110px;width:253px;height:40px">Schedule a Free Consultation</div>

<!-- why trust -->
<div class="title-rule" style="top:727px;left:480px;width:240px"></div>
<h2 class="section-title" style="top:740px">WHY CLIENTS TRUST <span class="accent">KBR LEGAL</span></h2>
<p class="lead" style="top:813px">Quis autem vel eum iure reprehenderit qui in ea voluptate velit esse quam nihil molestiae consequatur,<br>vel illum qui dolorem eum fugiat quo voluptas nulla pariatur</p>

<div class="trust-card" style="left:196px">
  <svg width="64" height="64" viewBox="0 0 64 64"><g fill="#2e8b2e"><circle cx="32" cy="30" r="7"/><circle cx="18" cy="36" r="5"/><circle cx="46" cy="36" r="5"/><path d="M20 58c0-9 5-15 12-15s12 6 12 15z"/><path d="M8 58c0-7 4-12 10-12 2 0 4 .5 5 1.5-2 3-3 6-3 10.5z"/><path d="M56 58c0-7-4-12-10-12-2 0-4 .5-5 1.5 2 3 3 6 3 10.5z"/><polygon points="32,2 35,9 42,9 36,13 38,20 32,16 26,20 28,13 22,9 29,9"/><polygon points="14,12 16,16 20,16 17,19 18,23 14,21 10,23 11,19 8,16 12,16"/><polygon points="50,12 52,16 56,16 53,19 54,23 50,21 46,23 47,19 44,16 48,16"/></g></svg>
  <h3>Experienced Attorneys</h3>
  <p>Ut enim ad minima veniam, quis no strum exercitationem ullam cor p oris suscipit labori</p>
  <a>Learn More</a>
</div>
<div class="trust-card active" style="left:475px">
  <svg width="64" height="64" viewBox="0 0 64 64"><g fill="#2e8b2e"><rect x="10" y="4" width="30" height="22" rx="4"/><polygon points="16,26 24,26 14,34"/><circle cx="18" cy="40" r="6"/><circle cx="46" cy="34" r="6"/><path d="M6 60c0-8 5-13 12-13s12 5 12 13z"/><path d="M34 60c0-8 5-13 12-13s12 5 12 13z"/><rect x="40" y="10" width="16" height="14" rx="3"/></g><path d="M18 15l5 5 9-9" stroke="#fff" stroke-width="3" fill="none"/></svg>
  <h3>Transparent Communication</h3>
  <p>Ut enim ad minima veniam, quis no strum exercitationem ullam cor p oris suscipit labori</p>
  <a>Learn More</a>
</div>
<div class="trust-card" style="left:754px">
  <svg width="64" height="64" viewBox="0 0 64 64"><path fill="#2e8b2e" d="M32 2l24 9v18c0 15-10 27-24 33C18 56 8 44 8 29V11z"/><path d="M21 31l8 8 14-15" stroke="#fff" stroke-width="4" fill="none"/></svg>
  <h3>Proven Track Record</h3>
  <p>Ut enim ad minima veniam, quis no strum exercitationem ullam cor p oris suscipit labori</p>
  <a>Learn More</a>
</div>

<!-- about -->
<svg class="abs" style="top:1443px;left:0" width="490" height="373"><polygon points="0,0 112,0 112,265 375,265 488,373 0,373" fill="#231f20"/></svg>
<div class="abs" style="top:1288px;left:112px;width:487px;height:416px;background:linear-gradient(135deg,#b9bcbf,#7f858b 55%,#2d3a52)" role="img" aria-label="Photograph of three lawyers in business suits posing together"></div>
<div class="title-rule" style="top:1311px;left:689px;width:120px"></div>
<h2 class="abs about-title">ABOUT <span style="color:var(--green)">KBR LEGAL</span></h2>
<p class="abs about-copy" style="top:1396px">Quis autem vel eum iure reprehenderit qui in ea voluptate velit esse quam nihil molestiae consequatur, vel illum qui dolorem eum fugiat quo voluptas nulla pariatur</p>
<p class="abs about-copy" style="top:1498px">Neque porro quisquam est, qui dolorem ipsum quia dolor sit amet, consectetur, adipisci velit, sed quia non numquam eius modi tempora incidunt ut labore et dolore magnam aliquam quaerat voluptatem.</p>
<div class="btn" style="top:1640px;left:689px;width:145px;height:42px">Read More</div>

<!-- services -->
<section class="abs services"></section>
<div class="title-rule" style="top:1868px;left:524px;width:152px"></div>
<h2 class="section-title" style="top:1881px">SERVICES WE <span class="accent">OFFER</span></h2>
<p class="lead" style="top:1954px">Quis autem vel eum iure reprehenderit qui in ea voluptate velit esse quam nihil molestiae consequatur,<br>vel illum qui dolorem eum fugiat quo voluptas nulla pariatur</p>

<div class="service-card" style="left:112px;width:226px">
  <div class="service-media" style="background:linear-gradient(135deg,#e2e5e8,#8c959c)" role="img" aria-label="Photograph of a hand touching a digital insurance interface"></div>
  <h3>COMMERCIAL LAW</h3><p>Ut enim ad minima veniam, quis no strum exercitationem ullam corporis suscip</p>
</div>
<div class="service-card active" style="left:360px;width:230px">
  <div class="service-media" style="background:linear-gradient(135deg,#5a4a3e,#d8d2c8 60%,#f2efe9)" role="img" aria-label="Photograph of a hand signing a document with a pen"></div>
  <h3>WILL LAW</h3><p>Ut enim ad minima veniam, quis no strum exercitationem ullam corporis suscip</p>
</div>
<div class="service-card" style="left:611px;width:227px">
  <div class="service-media" style="background:linear-gradient(180deg,#8fb8e6,#c9c7c0 55%,#8a9a6a)" role="img" aria-label="Photograph of modern apartment buildings along a garden path"></div>
  <h3>PROPERTY LAW</h3><p>Ut enim ad minima veniam, quis no strum exercitationem ullam corporis suscip</p>
</div>
<div class="service-card" style="left:860px;width:227px">
  <div class="service-media" style="background:linear-gradient(180deg,#6c7fa8,#e8a07a 55%,#b84a36)" role="img" aria-label="Photograph of a cargo plane above a truck and shipping containers at sunset"></div>
  <h3>CONVEYANCING</h3><p>Ut enim ad minima veniam, quis no strum exercitationem ullam corporis suscip</p>
</div>
<div class="round-arrow" style="top:2385px;left:553px;background:#d6d9d4"><svg width="10" height="10" viewBox="0 0 10 10"><path d="M7 1L3 5l4 4" stroke="#333" stroke-width="1.5" fill="none"/></svg></div>
<div class="round-arrow" style="top:2385px;left:605px;background:var(--dark)"><svg width="10" height="10" viewBox="0 0 10 10"><path d="M3 1l4 4-4 4" stroke="#fff" stroke-width="1.5" fill="none"/></svg></div>

<!-- testimonials -->
<svg class="abs reviews" width="1200" height="464"><rect width="1200" height="464" fill="#2e8b2e"/><polygon points="0,0 110,0 350,464 0,464" fill="#231f20"/></svg>
<div class="title-rule" style="top:2541px;left:121px;width:155px"></div>
<h2 class="abs" style="top:2553px;left:121px;font-family:'Roboto',sans-serif;font-weight:700;font-size:36px;color:#fff">OUR HAPPY CUSTOMERS</h2>
<div class="title-rule" style="top:2604px;left:121px;width:155px;background:#fff"></div>
<div class="round-arrow" style="top:2554px;left:982px;background:rgba(0,0,0,.12)"><svg width="10" height="10" viewBox="0 0 10 10"><path d="M7 1L3 5l4 4" stroke="#4d8d4d" stroke-width="1.5" fill="none"/></svg></div>
<div class="round-arrow" style="top:2554px;left:1034px;background:var(--dark)"><svg width="10" height="10" viewBox="0 0 10 10"><path d="M3 1l4 4-4 4" stroke="#fff" stroke-width="1.5" fill="none"/></svg></div>

<article class="review-card" style="left:124px">
  <div class="review-avatar" style="background:linear-gradient(160deg,#e9eaec,#9a8878)" role="img" aria-label="Portrait photo of a smiling client"></div>
  <div class="quote-badge">”</div>
  <p class="review-text">Neque porro quisquam est, qui dolorem ipsum quia dolor sit amet, consectetur, adipisci velit, sed quia non numquam eius modi tempora incidunt ut labore et dolore magnam aliquam quaerat voluptatem.</p>
  <div class="review-name">Daniel Reeve<span class="stars">★★★★☆</span></div>
  <div class="review-time">Few seconds ago</div>
</article>
<article class="review-card" style="left:611px">
  <div class="review-avatar" style="background:linear-gradient(160deg,#b9c6d4,#d2a24a)" role="img" aria-label="Portrait photo of a smiling client in an office"></div>
  <div class="quote-badge">”</div>
  <p class="review-text">Neque porro quisquam est, qui dolorem ipsum quia dolor sit amet, consectetur, adipisci velit, sed quia non numquam eius modi tempora incidunt ut labore et dolore magnam aliquam quaerat voluptatem.</p>
  <div class="review-name">Priya Nandan<span class="stars">★★★★☆</span></div>
  <div class="review-time">Few seconds ago</div>
</article>

<!-- experts -->
<h2 class="section-title" style="top:3026px">SPEAK TO AN <span class="accent">EXPERT</span></h2>
<p class="lead" style="top:3099px">Quis autem vel eum iure reprehenderit qui in ea voluptate velit esse quam nihil molestiae consequatur,<br>vel illum qui dolorem eum fugiat quo voluptas nulla pariatur</p>

<div class="expert-card" style="left:109px">
  <div class="expert-photo" style="background:linear-gradient(160deg,#8a6a4e,#2f3440)" role="img" aria-label="Portrait photo of a lawyer at a desk"></div>
  <h3>DANIEL REEVE</h3><div class="expert-role">Lawyer</div>
  <p>Quis autem vel eum iure reprehenderit qui in ea voluptate velit esse quam nihil...</p>
</div>
<div class="expert-card" style="left:360px">
  <div class="expert-photo" style="background:linear-gradient(160deg,#dfe3e6,#34465e)" role="img" aria-label="Portrait photo of a lawyer holding a tablet"></div>
  <h3>LAURA BENNET</h3><div class="expert-role">Lawyer</div>
  <p>Quis autem vel eum iure reprehenderit qui in ea voluptate velit esse quam nihil...</p>
</div>
<div class="expert-card active" style="left:611px">
  <div class="expert-photo" style="background:linear-gradient(160deg,#e6e6e6,#5a5f6a)" role="img" aria-label="Portrait photo of a lawyer in a white shirt"></div>
  <h3>MARCUS HALE</h3><div class="expert-role">Lawyer</div>
  <p>Quis autem vel eum iure reprehenderit qui in ea voluptate velit esse quam nihil...</p>
</div>
<div class="expert-card" style="left:863px">
  <div class="expert-photo" style="background:linear-gradient(160deg,#b07a4a,#22324a)" role="img" aria-label="Portrait photo of two lawyers together"></div>
  <h3>OWEN CLARKE</h3><div class="expert-role">Lawyer</div>
  <p>Quis autem vel eum iure reprehenderit qui in ea voluptate velit esse quam nihil...</p>
</div>
<div class="btn" style="top:3542px;left:472px;width:255px;height:42px">Schedule a Free Consultation</div>

<!-- footer -->
<footer class="abs footer">
  <div class="abs" style="top:58px;left:112px;font-family:'Roboto',sans-serif;font-weight:500;font-size:42px;letter-spacing:1px">KBR LEGAL</div>
  <div class="social" style="left:112px"></div>
  <div class="social" style="left:157px"></div>
  <div class="social" style="left:202px"></div>
  <div class="social" style="left:247px"></div>

  <h4 style="left:395px">QUICK LINKS</h4>
  <ul style="left:395px;top:98px">
    <li><span>»</span>Home</li><li><span>»</span>About KBR Legal</li><li><span>»</span>Testimonials</li><li><span>»</span>Blogs</li><li><span>»</span>Contact Us</li>
  </ul>

  <h4 style="left:601px">CONTACT US</h4>
  <ul style="left:601px;top:98px">
    <li><svg width="11" height="14" viewBox="0 0 12 16"><path fill="#fff" d="M6 0a6 6 0 016 6c0 4-6 10-6 10S0 10 0 6a6 6 0 016-6z"/><circle cx="6" cy="6" r="2" fill="#1d1f22"/></svg>41B, Harbour Lane, lorem lips</li>
    <li style="padding-left:27px">USA 560112</li>
    <li></li>
    <li><svg width="12" height="12" viewBox="0 0 24 24"><path fill="#fff" d="M6.6 10.8a15 15 0 006.6 6.6l2.2-2.2c.3-.3.7-.4 1-.2 1.1.4 2.3.6 3.6.6.6 0 1 .4 1 1V20c0 .6-.4 1-1 1A17 17 0 013 4c0-.6.4-1 1-1h3.5c.6 0 1 .4 1 1 0 1.3.2 2.5.6 3.6.1.3 0 .7-.2 1z"/></svg>Tel: +1 555 014 (2390)</li>
    <li><svg width="12" height="10" viewBox="0 0 24 20"><path fill="#fff" d="M2 2h20v16H2z"/><path fill="none" stroke="#1d1f22" stroke-width="2" d="M2 3l10 8 10-8"/></svg>Email: info@kbrlegal-demo.com</li>
  </ul>

  <h4 style="left:884px">FIND US</h4>
  <div class="abs" style="top:98px;left:884px;width:205px;height:142px;background:linear-gradient(135deg,#e4eee6,#cfdde8);border:2px solid #fff" role="img" aria-label="Map showing the office location"></div>
</footer>
<div class="abs copyright">(C) Copyright | All Rights Reserved</div>

</body>
</html>
```